Looking for a website design for my company
Services we offer:
Phone Repair
TV Mounting
Security Camera Installation
Networking / Wi-Fi
Smart Home Services
IT Support

Looking for a website similar to qarnel.com

Few tabs
About Us
Contact Us
Areas Served
Pricing and Services

```html
<!DOCTYPE html>
<html lang="en">
<head>
<meta charset="utf-8">
<title>Vanto Rim – Appliance Repair</title>
<link href="https://fonts.googleapis.com/css2?family=Ubuntu:wght@400;500;700&display=swap" rel="stylesheet">
<style>
  :root {
    --teal-deep: #0b4862;
    --teal-dark: #083a52;
    --brick: #6e5646;
    --brick-dark: #4e3c31;
    --orange: #f7931e;
    --navy-text: #0b3d57;
    --body-text: #3a3a3a;
    --icon-blue: #1f6fe0;
    --white: #ffffff;
  }
  * { box-sizing: border-box; margin: 0; padding: 0; }
  html, body { width: 1200px; height: 910px; overflow: hidden; background: var(--white); }
  body { font-family: "Ubuntu", sans-serif; position: relative; }

  .hero {
    position: absolute; left: 0; top: 0; width: 1200px; height: 457px;
    background: linear-gradient(180deg, var(--teal-dark) 0%, var(--teal-deep) 100%);
  }
  .hero-photo-building {
    position: absolute; left: 0; top: 143px; width: 816px; height: 314px;
    background: linear-gradient(180deg, var(--brick) 0%, var(--brick-dark) 100%);
  }

  .site-header { position: absolute; left: 0; top: 0; width: 1200px; height: 50px; }
  .brand {
    position: absolute; left: 140px; top: 6px;
    font-weight: 700; font-size: 34px; color: var(--orange); letter-spacing: -0.5px;
  }
  .main-nav { position: absolute; top: 17px; left: 0; }
  .main-nav a {
    position: absolute; white-space: nowrap; text-decoration: none;
    color: var(--white); font-weight: 700; font-size: 13px; text-transform: uppercase;
  }

  .hero-card {
    position: absolute; left: 140px; top: 118px; width: 419px; height: 228px;
    background: var(--white); padding: 30px 20px 0 15px;
  }
  .hero-card h1 { font-size: 32px; font-weight: 700; color: var(--navy-text); line-height: 1; }
  .hero-card p { margin-top: 14px; font-size: 18px; line-height: 27px; color: var(--body-text); width: 360px; }
  .btn-book {
    position: absolute; left: 16px; top: 151px; width: 191px; height: 38px;
    border-radius: 19px; background: var(--orange); color: var(--white);
    font-size: 13px; font-weight: 500; display: flex; align-items: center; justify-content: center;
    text-decoration: none;
  }

  .services { position: absolute; left: 0; top: 457px; width: 1200px; height: 453px; }
  .service { position: absolute; top: 78px; width: 160px; margin-left: -80px; text-align: center; }
  .service svg { width: 78px; height: 78px; display: block; margin: 0 auto; }
  .service-label { margin-top: 20px; font-size: 13.5px; line-height: 20px; color: var(--body-text); }
</style>
</head>
<body>
  <section class="hero">
    <div class="hero-photo-building" role="img" aria-label="Photo of a brick office building against a deep teal sky"></div>

    <header class="site-header">
      <div class="brand">Vanto Rim</div>
      <nav class="main-nav">
        <a href="#" style="left:542px">About Us</a>
        <a href="#" style="left:653px">Contact Us</a>
        <a href="#" style="left:777px">Areas Served</a>
        <a href="#" style="left:919px">Pricing &amp; Services</a>
      </nav>
    </header>

    <div class="hero-card">
      <h1>Repair Your Appliances</h1>
      <p>Repair your home appliances by highky trained professional technicians</p>
      <a class="btn-book" href="#">Book a Service</a>
    </div>
  </section>

  <section class="services">
    <div class="service" style="left:197px">
      <svg viewBox="0 0 60 60" fill="none" stroke="var(--icon-blue)" stroke-width="2" stroke-linecap="round" stroke-linejoin="round">
        <rect x="22" y="3" width="22" height="52" rx="3"/>
        <line x1="22" y1="10" x2="44" y2="10"/><line x1="22" y1="46" x2="44" y2="46"/>
        <path d="M3 26h18v6H3z"/><circle cx="34" cy="29" r="5"/><line x1="27" y1="38" x2="40" y2="38"/>
        <circle cx="27" cy="50" r="1.5"/><circle cx="33" cy="50" r="1.5"/><circle cx="39" cy="50" r="1.5"/>
      </svg>
      <div class="service-label">Mobile Repair</div>
    </div>
    <div class="service" style="left:378px">
      <svg viewBox="0 0 60 60" fill="none" stroke="var(--icon-blue)" stroke-width="2" stroke-linecap="round" stroke-linejoin="round">
        <path d="M22 8l34 16-6 12-34-16z"/>
        <path d="M24 26l-4 8 10 5"/>
        <line x1="20" y1="34" x2="10" y2="34"/>
        <rect x="5" y="26" width="5" height="22"/>
        <circle cx="47" cy="27" r="2"/>
      </svg>
      <div class="service-label">Security Camera<br>Installationa</div>
    </div>
    <div class="service" style="left:598px">
      <svg viewBox="0 0 60 60" fill="none" stroke="var(--icon-blue)" stroke-width="2" stroke-linecap="round" stroke-linejoin="round">
        <rect x="4" y="14" width="20" height="28" rx="3"/>
        <path d="M8 14V4h12v10M8 42v12h12V42"/>
        <circle cx="14" cy="28" r="5"/>
        <path d="M30 18l14-12 14 12M33 16v20h22V16"/>
        <rect x="40" y="24" width="8" height="12"/>
        <path d="M24 48h20"/><circle cx="49" cy="48" r="6"/>
      </svg>
      <div class="service-label">Smart Home<br>Services</div>
    </div>
    <div class="service" style="left:803px">
      <svg viewBox="0 0 60 60" fill="none" stroke="var(--icon-blue)" stroke-width="2" stroke-linecap="round" stroke-linejoin="round">
        <rect x="3" y="10" width="54" height="34" rx="2"/>
        <rect x="7" y="14" width="46" height="26"/>
        <path d="M26 44l-3 7M34 44l3 7M18 51h24"/>
      </svg>
      <div class="service-label">T.V Mounting</div>
    </div>
    <div class="service" style="left:1003px">
      <svg viewBox="0 0 60 60" fill="none" stroke="var(--icon-blue)" stroke-width="2" stroke-linecap="round" stroke-linejoin="round">
        <path d="M3 20a38 38 0 0 1 54 0"/>
        <path d="M10 27a28 28 0 0 1 40 0"/>
        <path d="M17 34a18 18 0 0 1 26 0"/>
        <path d="M24 41a8 8 0 0 1 12 0"/>
        <circle cx="30" cy="49" r="2.5"/>
      </svg>
      <div class="service-label">Netwroking /<br>Wi-Fi</div>
    </div>
  </section>
</body>
</html>
```